Brelton Packaging Supplies - A manufacturer of various packaging products

We have a large catalog of products and are transitioning to Shopify for our e-commerce side of business. Our products have been imported and the backend admin work has been completed, but we want to get professional graphic design done for the website to seem more professional. We are aiming for something similar to kestrovo.com and dapplewick.com. There are several more reference examples we can provide upon request. We have files of our product pictures, logos, etc. that can be used but we are looking to implement new and professional graphics throughout the website. Our current mock website is breltonpackagingsupplies.examplestore.com which contains our product listings and logo and other relevant information.
Target Market(s)
Primarily B2B, but we also have a good share of B2C customers
Industry/Entity Type
Manufacturing, Packaging Supplies
Requirements
Must have
- Professional appearance that is uniform throughout the website.
Nice to have
- Product details, emphasize our free shipping on any order, emphasize made in the USA
Should not have
- No typos or grammatical errors.

```html
<!DOCTYPE html>
<html lang="en">
<head>
<meta charset="utf-8">
<title>Brelton Packaging Supplies</title>
<link href="https://fonts.googleapis.com/css2?family=Barlow:wght@400;500;600;700&display=swap" rel="stylesheet">
<style>
:root{
  --ink:#111;
  --muted:#444;
  --purple:#5b2e8f;
  --magenta:#c21c7a;
  --star:#f4a300;
  --card:#f4f4f4;
  --orange:#f38a1d;
  --footer:#000;
}
*{box-sizing:border-box;margin:0;padding:0}
html,body{width:1200px;height:3525px;overflow:hidden}
body{position:relative;background:#fff;font-family:'Barlow',sans-serif;color:var(--ink)}
.abs{position:absolute}
.topbar{left:0;top:0;width:1200px;height:52px;background:linear-gradient(90deg,#f7a21b,#f3e21b 18%,#5bbf4a 35%,#14a6a0 52%,#2b6fd0 68%,#8a3fb5 84%,#e2204f)}
.topbar .ship{left:632px;top:16px;color:#fff;font-weight:600;font-size:16px}
.topbar .sep{left:884px;top:12px;width:1px;height:28px;background:#fff}
.topbar .sub{left:940px;top:17px;color:#fff;font-size:13px;font-weight:600;display:flex;align-items:center;gap:6px}
.navbar{left:0;top:52px;width:1200px;height:82px;background:#fff;border-bottom:1px solid #ddd}
.logo-box{left:111px;top:16px;width:264px;height:130px;background:#fff;border-radius:8px;z-index:3;display:flex;flex-direction:column;align-items:center;justify-content:center;gap:8px;box-shadow:0 1px 4px rgba(0,0,0,.08)}
.logo-box .dot{width:40px;height:40px;border-radius:50%;background:var(--purple)}
.logo-box span{font-size:21px;color:var(--orange);font-weight:500}
.nav a{position:absolute;font-size:15px;color:#222;text-decoration:none}
.search{left:903px;top:74px;width:186px;height:28px;border-bottom:1px solid #888;font-size:13px;color:#444;padding-top:4px}
.search svg{position:absolute;right:2px;top:4px}
.hero{left:0;top:134px;width:1200px;height:599px;background:radial-gradient(ellipse at 45% 50%,#e0a322 0%,#c58a24 30%,transparent 60%),linear-gradient(120deg,#5e636b,#8d7a52 35%,#a67c45 60%,#4f5660)}
.hero h1{position:absolute;left:0;top:120px;width:1200px;text-align:center;color:#fff;font-size:54px;line-height:61px;font-weight:700;text-transform:uppercase;text-shadow:0 2px 6px rgba(0,0,0,.35)}
.btn-hero{left:528px;top:326px;width:144px;height:49px;border-radius:25px;background:var(--purple);color:#fff;font-weight:600;font-size:15px;display:flex;align-items:center;justify-content:center}
.dots{display:flex;gap:5px}
.dots i{width:10px;height:10px;border-radius:50%;background:#fff;display:block}
.dots i.on{background:#f3a21b;border:2px solid #fff}
.section-title{left:0;width:1200px;text-align:center;font-size:33px;font-weight:700}
.pcard{width:222px;height:281px;background:var(--card);text-align:center}
.pcard .ph{position:absolute;left:36px;top:35px;width:150px;height:130px;border-radius:50%;filter:blur(6px)}
.pcard h3{position:absolute;left:0;top:207px;width:100%;font-size:15px;font-weight:600}
.pcard .stars{position:absolute;left:0;top:237px;width:100%;color:var(--star);font-size:13px;letter-spacing:2px}
.gdots{display:flex;gap:4px}
.gdots i{width:10px;height:10px;border-radius:50%;background:#aaa;display:block}
.gdots i.on{background:#fff;border:2px solid #e2204f}
.band{left:0;top:1633px;width:1200px;height:426px;background:linear-gradient(100deg,#c2187a,#8a2a8f 55%,#5a2f95)}
.fcard{top:1718px;width:236px;background:#fff;border-radius:4px;text-align:center;padding:22px 22px 0}
.fcard .ic{width:58px;height:58px;margin:0 auto 20px;display:block}
.fcard h3{font-size:17px;font-weight:600;line-height:27px;text-transform:uppercase}
.fcard p{font-size:12.5px;line-height:21px;color:var(--muted);margin-top:10px;letter-spacing:.2px}
.bimg{width:279px;height:200px}
.bcard{background:#fff;box-shadow:0 2px 10px rgba(0,0,0,.08);padding:20px 18px}
.bcard h3{font-size:21px;line-height:30px;font-weight:600;color:#111}
.bcard p{font-size:13px;line-height:26px;color:#333;margin-top:10px}
.bcard a{display:block;margin-top:8px;font-size:13px;font-weight:600;color:var(--magenta);text-decoration:none}
.nl-sub{left:0;width:1200px;text-align:center;font-size:17px;font-weight:600;line-height:27px;text-transform:uppercase}
.nl-input{left:282px;top:2915px;width:480px;height:60px;background:#f1f1f1;font-size:12px;padding:23px 30px;color:#333}
.nl-btn{left:769px;top:2915px;width:149px;height:60px;background:var(--magenta);color:#fff;font-weight:600;font-size:15px;display:flex;align-items:center;justify-content:center}
.footer{left:0;top:3093px;width:1200px;height:432px;background:var(--footer);color:#fff}
.flogo{left:115px;top:95px;display:flex;flex-direction:column;align-items:center;gap:10px;width:300px}
.flogo .dot{width:60px;height:60px;border-radius:50%;background:var(--purple)}
.flogo span{font-size:27px;color:var(--orange)}
.footer h4{position:absolute;top:90px;font-size:21px;font-weight:600;text-transform:uppercase}
.contact{left:486px;top:132px;font-size:15px;line-height:24px}
.contact div{display:flex;gap:8px;margin-bottom:12px}
.contact svg{flex:none;margin-top:5px}
.menu{left:784px;top:132px;font-size:15px;line-height:30px}
.social{left:955px;top:135px;display:flex;gap:9px}
.social i{display:block;width:31px;height:31px;border-radius:50%;background:#fff;border:7px solid #fff;box-shadow:inset 0 0 0 2px #c21c7a}
.social i.first{background:var(--purple);border-color:var(--purple);box-shadow:inset 0 0 0 2px #fff}
.fline{left:115px;top:338px;width:990px;height:1px;background:#333}
.copy{left:0;top:376px;width:1200px;text-align:center;font-size:15px}
</style>
</head>
<body>

<div class="abs topbar">
  <div class="abs ship">FREE Shipping On All Orders!</div>
  <div class="abs sep"></div>
  <div class="abs sub"><svg width="14" height="11" viewBox="0 0 14 11"><rect width="14" height="11" rx="1" fill="#fff"/><path d="M0 1 L7 6 L14 1" stroke="#b0306a" fill="none"/></svg>Subscribe &amp; Save</div>
</div>

<header class="abs navbar">
  <nav class="nav">
    <a style="left:499px;top:30px">Home</a>
    <a style="left:577px;top:30px">Catalog</a>
    <a style="left:665px;top:30px">About Us</a>
    <a style="left:765px;top:30px">Contact Us</a>
  </nav>
</header>
<div class="abs logo-box"><div class="dot"></div><span>Brelton Packaging Supplies</span></div>
<div class="abs search">Search
  <svg width="16" height="16" viewBox="0 0 16 16"><circle cx="6.5" cy="6.5" r="5" stroke="#111" stroke-width="2" fill="none"/><line x1="10" y1="10" x2="15" y2="15" stroke="#111" stroke-width="2.2"/></svg>
</div>

<section class="abs hero" role="img" aria-label="Packaging line wrapping boxes in yellow stretch film">
  <h1>Your products,<br>our pride uncompromised<br>quality packaging.</h1>
  <div class="abs btn-hero">LEARN MORE</div>
  <div class="abs dots" style="left:570px;top:534px"><i></i><i></i><i class="on"></i><i></i><i></i></div>
</section>

<h2 class="abs section-title" style="top:802px">PRODUCT LINES</h2>

<div class="abs pcard" style="left:111px;top:899px"><div class="ph" role="img" aria-label="Yellow padded mailers" style="background:radial-gradient(circle,#f5c531 0%,#e8b02e 55%,rgba(244,244,244,0) 72%)"></div><h3>MAILERS</h3><div class="stars">★★★★★</div></div>
<div class="abs pcard" style="left:363px;top:899px"><div class="ph" role="img" aria-label="Label rolls" style="background:radial-gradient(circle,#d6d6d6 0%,#e2e2e2 50%,rgba(244,244,244,0) 72%)"></div><h3>LABELS</h3><div class="stars">★★★★★</div></div>
<div class="abs pcard" style="left:615px;top:899px"><div class="ph" role="img" aria-label="Yellow bolt security seal" style="background:radial-gradient(circle,#e3dc3a 0%,#eae68a 45%,rgba(244,244,244,0) 70%)"></div><h3 style="top:210px">SECURITY SEALS</h3><div class="stars">★★★★★</div></div>
<div class="abs pcard" style="left:866px;top:899px"><div class="ph" role="img" aria-label="Roll of white tape" style="background:radial-gradient(circle,#fafafa 0%,#d4d4d4 50%,rgba(244,244,244,0) 72%)"></div><h3>TAPES</h3><div class="stars">★★★★★</div></div>

<div class="abs pcard" style="left:252px;top:1212px"><div class="ph" role="img" aria-label="Orange and green medicine vials" style="background:radial-gradient(circle,#6fb64a 0%,#f2b233 40%,rgba(244,244,244,0) 70%)"></div><h3>VIALS</h3><div class="stars">★★★★★</div></div>
<div class="abs pcard" style="left:503px;top:1212px"><div class="ph" role="img" aria-label="Packing list envelopes" style="background:radial-gradient(circle,#d9584a 0%,#f0e6e4 45%,rgba(244,244,244,0) 70%)"></div><h3>PACKING LISTS</h3><div class="stars">★★★★★</div></div>
<div class="abs pcard" style="left:755px;top:1212px"><div class="ph" role="img" aria-label="Stacked blue moving blankets" style="background:radial-gradient(circle,#2f5fc4 0%,#3c6fd0 50%,rgba(244,244,244,0) 72%)"></div><h3>MOVING BLANKETS</h3><div class="stars">★★★★★</div></div>

<div class="abs gdots" style="left:570px;top:1534px"><i></i><i></i><i class="on"></i><i></i><i></i></div>

<section class="abs band"></section>
<div class="abs fcard" style="left:114px;height:227px">
  <svg class="ic" viewBox="0 0 58 58"><circle cx="29" cy="29" r="29" fill="var(--orange)"/><rect x="10" y="20" width="24" height="16" rx="2" fill="#fff" stroke="#111" stroke-width="2"/><path d="M34 24h8l6 7v5H34z" fill="#fff" stroke="#111" stroke-width="2"/><circle cx="18" cy="39" r="4" fill="#fff" stroke="#111" stroke-width="2"/><circle cx="41" cy="39" r="4" fill="#fff" stroke="#111" stroke-width="2"/><path d="M14 28h16" stroke="#111" stroke-width="2"/></svg>
  <h3>Free &amp; fast shipping<br>nationwide</h3><p>All orders qualify for our premium free shipping service.</p></div>
<div class="abs fcard" style="left:360px;height:264px">
  <svg class="ic" viewBox="0 0 58 58"><circle cx="29" cy="29" r="29" fill="var(--orange)"/><rect x="17" y="12" width="22" height="32" rx="2" fill="#fff" stroke="#111" stroke-width="2"/><path d="M21 20h14M21 26h14M21 32h10" stroke="#111" stroke-width="2"/><circle cx="39" cy="40" r="7" fill="var(--orange)" stroke="#111" stroke-width="2"/><path d="M39 36v5l3 2" stroke="#111" stroke-width="2" fill="none"/></svg>
  <h3>Exceptional<br>customer care</h3><p>Our knowledgeable representatives are available to help with your personalized packaging needs.</p></div>
<div class="abs fcard" style="left:607px;height:263px">
  <svg class="ic" viewBox="0 0 58 58"><circle cx="29" cy="29" r="29" fill="var(--orange)"/><circle cx="29" cy="29" r="18" fill="none" stroke="#111" stroke-width="2" stroke-dasharray="4 3"/><circle cx="29" cy="29" r="11" fill="#fff" stroke="#111" stroke-width="2"/><path d="M24 29l4 4 7-8" stroke="#111" stroke-width="2.5" fill="none"/></svg>
  <h3>Hassle-free<br>returns policy</h3><p>Not happy with your order? No problem! Our simple return policy guarantees your satisfaction.</p></div>
<div class="abs fcard" style="left:854px;height:227px">
  <svg class="ic" viewBox="0 0 58 58"><circle cx="29" cy="29" r="29" fill="var(--orange)"/><rect x="10" y="18" width="30" height="20" rx="2" fill="#fff" stroke="#111" stroke-width="2"/><path d="M10 24h30M14 32h8" stroke="#111" stroke-width="2"/><path d="M42 24l8 3v6c0 5-4 8-8 9-4-1-8-4-8-9v-6z" fill="#fff" stroke="#111" stroke-width="2"/><path d="M39 33l2 2 4-4" stroke="#111" stroke-width="2" fill="none"/></svg>
  <h3>Secure payments</h3><p>Shop with confidence knowing that your payments are fully protected and secure.</p></div>

<h2 class="abs section-title" style="top:2120px">OUR BLOG</h2>

<div class="abs bimg" role="img" aria-label="Warehouse shelves stocked with boxes" style="left:126px;top:2223px;background:linear-gradient(135deg,#8a7f6a,#c7a64a 50%,#6b6860)"></div>
<article class="abs bcard" style="left:109px;top:2401px;width:312px;height:264px">
  <h3>Maximizing Savings: A Guide to Bulk Ordering and Cost-Effective Packaging</h3>
  <p>In today's competitive business landscape, optimizing costs while maintaining product quality is essential for sustainable growth.</p>
  <a>Learn More</a>
</article>

<article class="abs bcard" style="left:445px;top:2223px;width:310px;height:233px">
  <h3>The Role of Quality Packaging in Customer Experience and Retention</h3>
  <p style="height:78px;overflow:hidden">In the competitive world of ecommerce, where first impressions matter more than ever, the role of packaging extends far beyond simply</p>
  <a>Learn More</a>
</article>
<div class="abs bimg" role="img" aria-label="Delivery worker holding a cardboard box" style="left:460px;top:2465px;background:linear-gradient(135deg,#b9b3aa,#c99866 55%,#4d6a9a)"></div>

<div class="abs bimg" role="img" aria-label="Cardboard package with clipboard and stamp" style="left:795px;top:2223px;background:linear-gradient(135deg,#e8e4dc,#c7a57c 60%,#a78658)"></div>
<article class="abs bcard" style="left:778px;top:2401px;width:312px;height:264px">
  <h3>The Ultimate Guide to Choosing the Right Packaging Products for Your Business</h3>
  <p style="height:78px;overflow:hidden">In today's competitive marketplace, choosing the right packaging for your products is crucial. Not only does it protect your items</p>
  <a>Learn More</a>
</article>

<h2 class="abs section-title" style="top:2779px">NEWSLETTER</h2>
<div class="abs nl-sub" style="top:2832px">Receive frequent discounts and updates by<br>joining our newsletter!</div>
<div class="abs nl-input">ENTER YOUR EMAIL</div>
<div class="abs nl-btn">SUBSCRIBE</div>

<footer class="abs footer">
  <div class="abs flogo"><div class="dot"></div><span>Brelton Packaging Supplies</span></div>
  <h4 style="left:486px">Contact Us</h4>
  <div class="abs contact">
    <div><svg width="12" height="15" viewBox="0 0 12 15"><path d="M6 0a6 6 0 0 1 6 6c0 4-6 9-6 9S0 10 0 6a6 6 0 0 1 6-6z" fill="#fff"/><circle cx="6" cy="6" r="2" fill="#000"/></svg><span>4870 Harrow Lane,<br>Dunmore, OH, 45021</span></div>
    <div><svg width="13" height="13" viewBox="0 0 13 13"><path d="M3 0l2 3-1.5 1.5a8 8 0 0 0 5 5L10 8l3 2-1 3C6 13 0 7 0 1z" fill="#fff"/></svg><span>(555) 014-2298</span></div>
    <div style="margin-top:8px"><svg width="14" height="11" viewBox="0 0 14 11"><rect width="14" height="11" rx="1" fill="#fff"/><path d="M0 1 L7 6 L14 1" stroke="#000" fill="none"/></svg><span>info@breltonpackagingsupplies.com</span></div>
  </div>
  <h4 style="left:780px">Main Menu</h4>
  <div class="abs menu">Home<br>Catalog<br>About Us<br>Contact Us</div>
  <h4 style="left:955px">Follow Us</h4>
  <div class="abs social"><i class="first"></i><i></i><i></i><i></i></div>
  <div class="abs fline"></div>
  <div class="abs copy">©Copyrights 2024 Brelton Packaging Supplies | &nbsp; All Rights Reserved</div>
</footer>

</body>
</html>
```